Business card for a new cabinet shop company named Marlowe Cabinets for high end cabinets

Design a business card, thinking dark rich green with colours to speak of high end luxury ie; cream, gold, black possibly

Peter Lindqvar
Director Craftsman
Email: info@marlowecabinets.com.au
Instagram : @marlowe.cabinets

```html
<!DOCTYPE html>
<html lang="en">
<head>
<meta charset="utf-8">
<title>Marlowe Cabinets — Business Card</title>
<link rel="stylesheet" href="https://fonts.googleapis.com/css2?family=Poppins:wght@300;400&family=Tinos&display=swap">
<style>
  :root {
    --green: #0b4129;
    --gold-light: #f3d77a;
    --gold: #c9a24a;
    --gold-dark: #a7802f;
    --white: #ffffff;
    --page: #ffffff;
  }
  * { box-sizing: border-box; margin: 0; padding: 0; }
  html, body { width: 1152px; height: 1200px; overflow: hidden; background: var(--page); }
  .sheet {
    width: 1152px; height: 1200px;
    display: flex; align-items: center; justify-content: center; gap: 24px;
  }
  .card {
    position: relative; width: 541px; height: 300px;
    background: var(--green); overflow: hidden;
    font-family: "Poppins", sans-serif;
  }
  .card__band {
    position: absolute; left: 0; right: 0; height: 14px;
    background: linear-gradient(90deg, var(--gold-dark), var(--gold-light) 45%, var(--gold) 75%, var(--gold-dark));
  }
  .card__band--top { top: 0; }
  .card__band--bottom { bottom: 0; }

  .wordmark {
    position: absolute; display: flex; align-items: center;
    color: var(--gold);
  }
  .wordmark__dot {
    border: 2px solid var(--gold); border-radius: 50%; flex: none;
  }
  .wordmark__name { font-weight: 400; line-height: 1; }
  .wordmark__name span { display: block; }

  .card--front .wordmark { left: 50%; top: 50%; transform: translate(-50%, -50%); gap: 26px; }
  .card--front .wordmark__dot { width: 90px; height: 90px; }
  .card--front .wordmark__name .line-1 { font-size: 56px; letter-spacing: 1px; }
  .card--front .wordmark__name .line-2 { font-size: 27px; letter-spacing: 9px; margin-top: 8px; }

  .card--back .wordmark { left: 46px; top: 118px; gap: 14px; }
  .card--back .wordmark__dot { width: 46px; height: 46px; }
  .card--back .wordmark__name .line-1 { font-size: 30px; letter-spacing: 0.5px; }
  .card--back .wordmark__name .line-2 { font-size: 15px; letter-spacing: 5px; margin-top: 5px; }

  .person { position: absolute; right: 30px; top: 52px; text-align: right; white-space: nowrap; }
  .person__name { font-family: "Tinos", serif; font-size: 33px; color: var(--gold); line-height: 1; }
  .person__role { font-size: 12.5px; font-weight: 300; color: var(--white); margin-top: 8px; letter-spacing: 0.3px; }

  .divider {
    position: absolute; left: 297px; right: 0; top: 155px; height: 2px;
    background: linear-gradient(90deg, var(--gold), var(--gold-light));
  }

  .contacts { position: absolute; left: 297px; right: 20px; top: 192px; list-style: none; }
  .contacts__item {
    display: flex; align-items: center; gap: 12px; white-space: nowrap;
    font-size: 12.5px; color: var(--white); height: 24px; margin-bottom: 14px;
  }
  .contacts__icon {
    width: 22px; height: 22px; flex: none;
    background: linear-gradient(135deg, var(--gold-light), var(--gold-dark));
    display: flex; align-items: center; justify-content: center;
  }
</style>
</head>
<body>
<main class="sheet">
  <section class="card card--front" aria-label="Card front">
    <div class="card__band card__band--top"></div>
    <div class="wordmark">
      <div class="wordmark__dot"></div>
      <div class="wordmark__name"><span class="line-1">Marlowe</span><span class="line-2">CABINETS</span></div>
    </div>
    <div class="card__band card__band--bottom"></div>
  </section>

  <section class="card card--back" aria-label="Card back">
    <div class="card__band card__band--top"></div>
    <div class="wordmark">
      <div class="wordmark__dot"></div>
      <div class="wordmark__name"><span class="line-1">Marlowe</span><span class="line-2">CABINETS</span></div>
    </div>
    <div class="person">
      <p class="person__name">Peter Lindqvar</p>
      <p class="person__role">Director Craftsman</p>
    </div>
    <div class="divider"></div>
    <ul class="contacts">
      <li class="contacts__item">
        <span class="contacts__icon">
          <svg width="13" height="10" viewBox="0 0 14 11" aria-hidden="true">
            <rect x="0.75" y="0.75" width="12.5" height="9.5" fill="none" stroke="#0b4129" stroke-width="1.5"/>
            <path d="M1 1 L7 6 L13 1" fill="none" stroke="#0b4129" stroke-width="1.5"/>
          </svg>
        </span>
        info@marlowecabinets.com.au
      </li>
      <li class="contacts__item">
        <span class="contacts__icon"></span>
        @marlowe.cabinets
      </li>
    </ul>
    <div class="card__band card__band--bottom"></div>
  </section>
</main>
</body>
</html>
```